Realtor / Real Estate Lead Generation site

Need a website design for lead generation. This website connects realtors with buyers and sellers of homes. some sites i like are: quillmarsh.com, vanbridle.com, plumvestor.com. Those sites look nice and have the same purpose as mine. The name of my site is NestBridgeHub. Basically I connect people with Top producing real estate agents
Updates

Project Deadline Extended Reason: Im still waiting on all my friends to pick the design. I have sent them the link to view and comment. I will be committing payment as well. Added Monday, February 15, 2016

Target Market(s)

people looking to buy or sell a home

Industry/Entity Type

Real Estate

Coding

Coded - Design and coding required

Number of Pages Required

5+ page

Font styles to use
Sans Serif

Requirements
Must have
• 2 versions of a lead capture form. One for buyers and one for sellers. goto www.plumvestor.com and select "buyer", you will see a for asking for Price Range, Type of Home, and City or Zipcode. If you select seller it has a differnt set of questions. I like the way they have trust builders on the right hand side such as realtors faces and comments about the realtors.I would like trust builders above the fold as well, so when its viewed on a phone or computer they can see them without scrolling, something such as #1 company, please see quillmarsh-mobile.png file attached. I also have an explainer video that I would like a link to on the homepage above the fold without scrolling. please see brindlow.png file to see an example. I will upload video later. There should be a thank you page, privacy policy, terms and conditions. For ALL content see. www.789dwellmatch.com which is my current site.
• I would like the page to be mobile responsive/wordpress. Lastly, please see the form on 789dwellmatch.com. once you select the city, zipcode or address, and click "find my perfect agent, a form will come up with several different sets of questions. I would like that exact form used as I already paid for it on my other site. Thank you

```html
<!DOCTYPE html>
<html lang="en">
<head>
<meta charset="utf-8">
<title>NestBridgeHub – Lead Generation for Home Buyers and Sellers</title>
<link rel="stylesheet" href="https://fonts.googleapis.com/css2?family=Roboto:ital,wght@0,300;0,400;0,500;0,700;1,400&display=swap">
<style>
  :root {
    --blue: #1170bd;
    --blue-dark: #0b5a9c;
    --blue-light: #2a8ad6;
    --ink: #333333;
    --text: #555555;
    --muted: #999999;
    --line: #e2e2e2;
    --band: #f1f1f1;
    --soft: #f7f7f7;
    --footer: #333333;
    --white: #ffffff;
  }
  * { box-sizing: border-box; margin: 0; padding: 0; }
  html, body { width: 1200px; height: 2679px; overflow: hidden; }
  body { position: relative; font-family: "Roboto", Arial, sans-serif; color: var(--text); background: var(--white); }

  /* Header */
  .site-header { position: absolute; left: 0; top: 0; width: 1200px; height: 116px; background: var(--white); }
  .brand { position: absolute; left: 75px; top: 34px; display: flex; align-items: center; gap: 12px; }
  .brand-mark { width: 40px; height: 40px; background: var(--blue); border-radius: 4px; }
  .brand-name { font-size: 30px; font-weight: 500; color: var(--blue); letter-spacing: 0.3px; }
  .main-nav a { position: absolute; top: 50px; font-size: 14px; color: var(--ink); text-decoration: none; text-transform: uppercase; }
  .main-nav a.is-active { color: var(--blue); }
  .main-nav a.is-active::after { content: ""; position: absolute; left: -2px; right: -2px; top: 25px; height: 2px; background: var(--blue); }
  .auth-button { position: absolute; left: 970px; top: 43px; width: 155px; height: 36px; border: 2px solid var(--blue); border-radius: 3px; color: var(--blue); font-size: 13px; display: flex; align-items: center; justify-content: center; text-transform: uppercase; }

  /* Hero */
  .hero { position: absolute; left: 0; top: 116px; width: 1200px; height: 518px; overflow: hidden;
    background: linear-gradient(180deg, #3f67ad 0%, #6d93cf 55%, #9bb8e0 100%); }
  .hero-photo { position: absolute; left: 0; top: 0; width: 920px; height: 518px;
    background: linear-gradient(100deg, #2e2f33 0%, #c6a432 18%, #d6b53a 38%, #3c3e43 55%, rgba(60,62,67,0) 80%); }
  .slider-prev { position: absolute; left: 77px; top: 348px; width: 50px; height: 50px; border: 2px solid var(--white); border-radius: 50%; }
  .lead-form { position: absolute; left: 782px; top: 0; width: 336px; }
  .lead-form h1 { position: absolute; top: 68px; left: 0; width: 400px; font-size: 28px; font-weight: 400; line-height: 33px; color: var(--white); text-transform: uppercase; }
  .role-switch { position: absolute; top: 164px; left: 0; display: flex; gap: 24px; font-size: 15px; color: var(--white); text-transform: uppercase; }
  .role-switch span { display: flex; align-items: center; gap: 7px; }
  .radio { width: 11px; height: 11px; border: 1.5px solid var(--white); border-radius: 50%; }
  .radio.is-on { background: var(--white); box-shadow: inset 0 0 0 2px #7f9fd3; }
  .field { position: absolute; left: 0; width: 336px; height: 37px; border: 2px solid rgba(255,255,255,0.85); background: rgba(255,255,255,0.12); color: var(--white); font-size: 12px; padding-left: 17px; display: flex; align-items: center; }
  .cta { position: absolute; left: 0; top: 405px; width: 336px; height: 47px; background: linear-gradient(180deg, var(--blue-light), var(--blue)); color: var(--white); font-size: 16px; letter-spacing: 0.5px; display: flex; align-items: center; justify-content: center; text-transform: uppercase; }

  /* Section headings */
  .section-title { position: absolute; left: 0; width: 1200px; text-align: center; font-size: 28px; font-weight: 400; color: var(--blue); text-transform: uppercase; }

  /* Services */
  .services-intro { position: absolute; left: 0; top: 726px; width: 1200px; text-align: center; font-size: 17px; color: var(--ink); }
  .service-card { position: absolute; top: 814px; width: 332px; height: 277px; border: 1px solid var(--line); background: var(--white); }
  .service-photo { width: 100%; height: 172px; }
  .service-icon { position: absolute; left: 136px; top: -32px; width: 60px; height: 60px; border-radius: 50%; background: var(--blue); border: 5px solid var(--white); display: flex; align-items: center; justify-content: center; }
  .service-card h3 { margin-top: 20px; text-align: center; font-size: 19px; font-weight: 400; color: var(--blue); }
  .service-card p { margin: 10px auto 0; width: 290px; text-align: center; font-size: 14px; line-height: 18px; color: var(--text); }

  /* About */
  .about { position: absolute; left: 0; top: 1145px; width: 1200px; height: 328px; background: var(--band); }
  .about-kicker { position: absolute; top: 52px; width: 1200px; text-align: center; font-size: 28px; font-weight: 400; color: var(--ink); }
  .about-title { position: absolute; top: 84px; width: 1200px; text-align: center; font-size: 28px; font-weight: 400; color: var(--blue); text-transform: uppercase; }
  .about p { position: absolute; left: 84px; top: 136px; width: 1034px; text-align: center; font-size: 14px; line-height: 23px; color: var(--text); }
  .btn { position: absolute; height: 37px; display: flex; align-items: center; justify-content: center; color: var(--white); font-size: 14px; text-transform: uppercase; border-radius: 2px; }
  .btn-blue { background: var(--blue); }
  .btn-dark { background: #444444; }

  /* Split sections */
  .split { position: absolute; left: 0; width: 1200px; height: 367px; }
  .split-photo { position: absolute; top: 0; width: 600px; height: 367px; }
  .split-copy { position: absolute; top: 0; width: 600px; height: 367px; }
  .split-copy h2 { position: absolute; top: 50px; font-size: 27px; font-weight: 400; color: var(--blue); text-transform: uppercase; }
  .split-copy p { position: absolute; width: 496px; font-size: 14px; line-height: 22.5px; text-align: justify; color: var(--text); }
  .split-right h2 { right: 73px; }
  .split-right p { right: 73px; text-align-last: right; }

  /* Testimonials */
  .testimonials { position: absolute; left: 0; top: 2206px; width: 1200px; height: 402px; background: var(--soft); }
  .quote { position: absolute; left: 150px; top: 124px; width: 936px; text-align: center; font-size: 15px; font-style: italic; line-height: 26px; color: var(--ink); }
  .quote-mark { position: absolute; font-size: 60px; font-weight: 700; color: #d5d5d5; font-style: normal; line-height: 1; }
  .author { position: absolute; top: 219px; width: 1200px; text-align: center; font-size: 17px; color: var(--blue); }
  .author-city { position: absolute; top: 241px; width: 1200px; text-align: center; font-size: 12px; color: var(--muted); }
  .divider { position: absolute; left: 0; top: 316px; width: 1200px; height: 1px; background: var(--line); }
  .round-arrow { position: absolute; top: 294px; width: 40px; height: 40px; border-radius: 50%; display: flex; align-items: center; justify-content: center; }
  .avatar { position: absolute; left: 555px; top: 271px; width: 86px; height: 86px; border-radius: 50%; border: 4px solid var(--white); background: radial-gradient(circle at 50% 40%, #e8c9a8, #8a6a50); }

  /* Footer */
  .site-footer { position: absolute; left: 0; top: 2608px; width: 1200px; height: 71px; background: var(--footer); }
  .copyright { position: absolute; left: 71px; top: 28px; font-size: 13px; color: #e5e5e5; }
  .social { position: absolute; top: 21px; width: 29px; height: 29px; border: 1.5px solid #e5e5e5; border-radius: 50%; }
</style>
</head>
<body>

<header class="site-header">
  <div class="brand"><span class="brand-mark"></span><span class="brand-name">NestBridgeHub</span></div>
  <nav class="main-nav">
    <a class="is-active" href="#" style="left:443px">Home</a>
    <a href="#" style="left:525px">For Sellers</a>
    <a href="#" style="left:648px">For Buyers</a>
    <a href="#" style="left:773px">For Pros</a>
    <a href="#" style="left:879px">About Us</a>
  </nav>
  <div class="auth-button">Sign In \ Sign Up</div>
</header>

<section class="hero">
  <div class="hero-photo" role="img" aria-label="Modern yellow and dark grey apartment building against a blue sky"></div>
  <div class="slider-prev">
    <svg width="46" height="46" viewBox="0 0 46 46"><path d="M26 15 L18 23 L26 31" fill="none" stroke="#fff" stroke-width="2.5"/></svg>
  </div>
  <div class="lead-form">
    <h1>We are a lead<br>generation company</h1>
    <div class="role-switch">
      <span><i class="radio"></i>Buyer</span>
      <span><i class="radio is-on"></i>Seller</span>
    </div>
    <div class="field" style="top:200px">Enter your Name</div>
    <div class="field" style="top:250px">Enter your Email</div>
    <div class="field" style="top:302px">Enter your Company</div>
    <div class="field" style="top:354px">Enter your Phone No.</div>
    <div class="cta">Get Started</div>
  </div>
</section>

<h2 class="section-title" style="top:688px">Our Services</h2>
<p class="services-intro">We are a lead generation company. The company connects realtors with buyers and sellers of homes.</p>

<article class="service-card" style="left:75px">
  <div class="service-photo" role="img" aria-label="Agent handing house keys to a client" style="background:linear-gradient(135deg,#c9ccd1,#5a5d63 60%,#2b2c30)"></div>
  <div class="service-icon">
    <svg width="26" height="26" viewBox="0 0 26 26"><path d="M3 3 H12 L23 14 L14 23 L3 12 Z" fill="#fff"/><circle cx="8" cy="8" r="2" fill="#1170bd"/></svg>
  </div>
  <h3>Free and Unbiased</h3>
  <p>Neque porro quisquam est qui dolorem ipsum quia dolor sit amet, consec.</p>
</article>

<article class="service-card" style="left:434px">
  <div class="service-photo" role="img" aria-label="Smiling real estate agent with clients behind him" style="background:linear-gradient(135deg,#9fb37a,#6e5a48 45%,#b0332f 75%,#d6c7b5)"></div>
  <div class="service-icon">
    <svg width="26" height="26" viewBox="0 0 26 26"><circle cx="13" cy="8" r="5" fill="#fff"/><path d="M3 24 C3 16 23 16 23 24 Z" fill="#fff"/></svg>
  </div>
  <h3>Our Agents are top 5%</h3>
  <p>Neque porro quisquam est qui dolorem ipsum quia dolor sit amet, consec.</p>
</article>

<article class="service-card" style="left:793px">
  <div class="service-photo" role="img" aria-label="Alarm clock standing in green grass" style="background:linear-gradient(180deg,#dce6ef 0%,#c8d4dc 50%,#6fa13a 75%,#3d7a22 100%)"></div>
  <div class="service-icon">
    <svg width="26" height="26" viewBox="0 0 26 26"><path d="M5 13 A8 8 0 1 0 8 6.5" fill="none" stroke="#fff" stroke-width="2.5"/><path d="M4 4 L8 6.5 L5 10" fill="none" stroke="#fff" stroke-width="2.2"/><path d="M13 8 V13 L16 15" fill="none" stroke="#fff" stroke-width="2.2"/></svg>
  </div>
  <h3>Save Time and Hassle</h3>
  <p>Neque porro quisquam est qui dolorem ipsum quia dolor sit amet, consec.</p>
</article>

<section class="about">
  <div class="about-kicker">ABOUT</div>
  <div class="about-title">NestBridgeHub</div>
  <p>Neque porro quisquam est qui dolorem ipsum quia dolor sit amet, consec. Lorem Ipsum is simply dummy text of the printing and typesetting industry. Lorem Ipsum has been the industry's standard dummy text ever since the 1500s, when an unknown printer took a galley of type and scrambled it to make a type specimen book. It has survived not only five centuries, but also the leap into electronic typesetting, remaining essentially unchanged</p>
  <div class="btn btn-blue" style="left:439px;top:227px;width:152px">Read More</div>
  <div class="btn btn-dark" style="left:609px;top:227px;width:152px">Contact Us</div>
</section>

<section class="split" style="top:1473px">
  <div class="split-copy" style="left:0">
    <h2 style="left:73px">For Seller</h2>
    <p style="left:73px;top:104px">Neque porro quisquam est qui dolorem ipsum quia dolor sit amet, consec Ipsum is simply dummy text of the printing and typesetting industry. Lorem Ipsum has been the industry's standard dummy text</p>
    <p style="left:73px;top:200px">Ever since the 1500s, when an unknown printer took a galley of type and scrambled it to make a type specimen book. It has survived not only five centuries, but also the leap into electronic typesetting remaining.</p>
    <div class="btn btn-blue" style="left:75px;top:274px;width:139px">Learn More</div>
  </div>
  <div class="split-photo" style="left:600px;background:linear-gradient(180deg,#3b7fd0 0%,#8fbbe8 45%,#5d5a58 60%,#4a4744 78%,#4f8a2e 90%,#3f7a24 100%)" role="img" aria-label="Modern stone-clad house with lawn and palm trees"></div>
</section>

<section class="split split-right" style="top:1840px">
  <div class="split-photo" style="left:0;background:linear-gradient(120deg,#e9eef0 0%,#b8c4cc 35%,#d8b79a 55%,#f2f2f0 100%)" role="img" aria-label="Happy couple receiving the keys to their new home"></div>
  <div class="split-copy" style="left:600px">
    <h2>For Buyers</h2>
    <p style="top:104px">Neque porro quisquam est qui dolorem ipsum quia dolor sit amet, consec Ipsum is simply dummy text of the printing and typesetting industry. Lorem Ipsum has been the industry's standard dummy text</p>
    <p style="top:200px">Ever since the 1500s, when an unknown printer took a galley of type and scrambled it to make a type specimen book. It has survived not only five centuries, but also the leap into electronic typesetting remaining.</p>
    <div class="btn btn-blue" style="left:386px;top:271px;width:139px">Learn More</div>
  </div>
</section>

<section class="testimonials">
  <h2 class="section-title" style="top:68px">Testimonial's</h2>
  <span class="quote-mark" style="left:108px;top:112px">&ldquo;</span>
  <p class="quote">Neque porro quisquam est qui dolorem ipsum quia dolor sit amet, consec Ipsum is simply dummy text of the printing and typesetting industry. Lorem Ipsum has been the industry's standard dummy text, Ever since the 1500s, when an unknown printer took a galley of type and scrambled it to make a type specimen book. It has survived not only five centuries, but also the leap into electronic.</p>
  <span class="quote-mark" style="left:932px;top:178px">&rdquo;</span>
  <div class="author">By Author Name</div>
  <div class="author-city">City Location</div>
  <div class="divider"></div>
  <div class="round-arrow" style="left:494px;background:var(--blue)">
    <svg width="20" height="20" viewBox="0 0 20 20"><path d="M12 5 L7 10 L12 15" fill="none" stroke="#fff" stroke-width="2.2"/></svg>
  </div>
  <div class="avatar" role="img" aria-label="Portrait of the testimonial author"></div>
  <div class="round-arrow" style="left:664px;background:#444">
    <svg width="20" height="20" viewBox="0 0 20 20"><path d="M8 5 L13 10 L8 15" fill="none" stroke="#fff" stroke-width="2.2"/></svg>
  </div>
</section>

<footer class="site-footer">
  <div class="copyright">Copyright &copy; 2016 Yoursitename. All rights reserved.</div>
  <span class="social" style="left:983px"></span>
  <span class="social" style="left:1022px"></span>
  <span class="social" style="left:1061px"></span>
  <span class="social" style="left:1100px"></span>
</footer>

</body>
</html>
```